Bright Summit Consulting Website Design

I already have a live website. Just want some help with design, finishing up the project. I also have another site with wix that I am ready to have designed. I am not completely sure on the pages but will for sure need "coaching", "training", "resources". Most of the people I currently work with are real estate brokers and mortgage brokers but I want to be able to appeal to all industries.
Number of Pages Required
4 page
Font styles to use
Sans Serif
Colors
Designer to choose colors to be used in the design.
Requirements
Must have
- place holders for video
Nice to have
- a way for people to purchase digital downloads

```html
<!DOCTYPE html>
<html lang="en">
<head>
<meta charset="utf-8">
<title>Bright Summit Consulting — Website</title>
<link rel="stylesheet" href="https://fonts.googleapis.com/css2?family=Montserrat:wght@300;400;600;700;800&display=swap">
<style>
  :root{
    --red:#ec3b2f;
    --ink:#3f4044;
    --ink-soft:#8a8b8f;
    --dark:#434448;
    --darker:#38393c;
    --paper:#ffffff;
    --mist:#f4f5f5;
    --photo:#b9babd;
  }
  *{box-sizing:border-box;margin:0;padding:0}
  html,body{width:960px;height:1200px;overflow:hidden;background:var(--paper)}
  body{font-family:"Montserrat",sans-serif;color:var(--ink)}
  .stage{position:relative;width:960px;height:1200px;overflow:hidden}
  .site{position:absolute;left:335px;top:10px;width:352px;height:1432px;transform:scale(.824);transform-origin:0 0;background:var(--paper);overflow:hidden}
  .abs{position:absolute}

  /* header */
  .topbar{left:0;top:0;width:352px;height:25px;background:var(--paper)}
  .brand{left:12px;top:6px;display:flex;align-items:center;gap:4px}
  .brand-mark{width:12px;height:12px;background:var(--red)}
  .brand-name{font-size:4.4px;font-weight:400;color:var(--ink);line-height:1.35;white-space:nowrap}
  .brand-tag{display:block;font-size:3.2px;color:var(--ink)}
  .nav{right:10px;top:11px;display:flex;gap:5px;font-size:3.4px;color:var(--ink-soft)}

  /* hero */
  .hero{left:0;top:25px;width:352px;height:177px;background:linear-gradient(120deg,#e2392e 0%,#f0483b 45%,#d63126 100%)}
  .hero-title{left:0;top:52px;width:352px;text-align:center;color:#fff;font-size:17px;font-weight:300;letter-spacing:.3px}
  .hero-title b{font-weight:800}
  .hero-copy{left:78px;top:87px;width:196px;text-align:center;color:#fff;font-size:4.5px;line-height:1.55;font-weight:300}

  .mist-band{left:0;top:202px;width:352px;height:420px;background:var(--mist)}

  /* ghost words */
  .ghost{font-weight:800;letter-spacing:1px;white-space:nowrap;line-height:1}

  /* about */
  .about-card{left:33px;top:178px;width:286px;height:179px;background:var(--paper);box-shadow:0 1px 4px rgba(0,0,0,.14);border-radius:2px}
  .about-photo{left:53px;top:202px;width:117px;height:126px;background:linear-gradient(160deg,#d2d3d5,#8d8e91 70%,#6d6e71)}
  .play{left:91px;top:245px;width:40px;height:40px}
  .section-title{font-size:11px;font-weight:400;color:var(--ink);white-space:nowrap}
  .section-title span{color:var(--red)}
  .rule{height:1px;background:var(--red)}
  .about-title{left:186px;top:202px}
  .about-rule{left:138px;top:218px;width:98px}
  .about-copy{left:186px;top:230px;width:112px;font-size:4.3px;line-height:1.6;color:var(--ink-soft);font-weight:300}
  .ghost-about{left:157px;top:306px;font-size:34px;color:rgba(0,0,0,.035)}

  /* features */
  .ghost-feat{left:88px;top:393px;font-size:34px;color:rgba(255,255,255,.85)}
  .feat-title{left:32px;top:386px}
  .feat-rule{left:0;top:402px;width:109px}
  .feat-img{top:426px;height:87px}
  .feat-img.a{left:33px;width:88px;background:linear-gradient(180deg,#7a3b22,#b8553a 55%,#4d2b21)}
  .feat-img.b{left:133px;width:86px;background:linear-gradient(180deg,#d9dadd,#7d7f86 60%,#2e2f33)}
  .feat-img.c{left:231px;width:88px;background:linear-gradient(180deg,#c7cbd2,#8b8f99 55%,#5b5f68)}
  .feat-name{top:522px;width:88px;text-align:center;font-size:4.6px;color:var(--red);line-height:1.35;font-weight:400}
  .feat-copy{top:546px;width:84px;text-align:center;font-size:4px;line-height:1.55;color:var(--ink-soft);font-weight:300}

  /* stats */
  .stats{left:0;top:622px;width:352px;height:70px;background:var(--dark)}
  .stat{top:641px;width:70px;text-align:center}
  .stat-num{font-size:16px;font-weight:700;color:#fff;line-height:1}
  .stat-label{font-size:3.6px;color:var(--red);margin-top:5px}
  .cta{left:235px;top:637px;width:80px;height:80px;background:var(--red);text-align:center;color:#fff}
  .cta-kicker{font-size:5px;font-weight:300;margin-top:15px;letter-spacing:.2px}
  .cta-big{font-size:14px;font-weight:800;color:var(--ink);margin-top:1px}
  .pill{display:inline-block;border:.7px solid #fff;border-radius:6px;font-size:4px;padding:1.5px 10px;color:#fff}
  .cta .pill{margin-top:11px}

  /* book */
  .book-title{left:136px;top:718px}
  .book-rule{left:136px;top:735px;width:216px}
  .book-box{top:751px;height:86px;background:var(--photo)}
  .book-box .pill{position:absolute;left:50%;bottom:5px;transform:translateX(-50%);border-color:#e6e6e7;color:#eee;padding:1.5px 14px}

  /* testimonials */
  .testi{left:0;top:875px;width:352px;height:136px;background:var(--mist)}
  .ghost-testi{left:92px;top:902px;font-size:25px;color:rgba(255,255,255,.9)}
  .testi-title{left:32px;top:892px}
  .testi-rule{left:0;top:908px;width:136px}
  .quote{left:55px;top:945px;width:242px;text-align:center;font-size:4.5px;line-height:1.5;color:var(--ink-soft);font-weight:300}
  .quote-by{left:0;top:972px;width:352px;text-align:center;font-size:5px;color:var(--red)}
  .dots{left:170px;top:986px;display:flex;gap:2px}
  .dots i{width:2.5px;height:2.5px;border-radius:50%;background:#c6c7c9;display:block}
  .dots i.on{background:var(--red)}

  /* blog */
  .blog{left:0;top:1011px;width:352px;height:182px;background:var(--dark)}
  .ghost-news{left:35px;top:1030px;font-size:34px;color:var(--darker);letter-spacing:0}
  .blog-title{left:36px;top:1057px;font-size:11px;color:#fff;font-weight:400}
  .blog-title span{color:var(--red)}
  .blog-rule{left:0;top:1073px;width:91px}
  .post{top:1087px;width:88px;height:84px}
  .post.a{left:37px;background:linear-gradient(160deg,#d6dbe1,#8e97a3 60%,#5a6270)}
  .post.b{left:131px;background:linear-gradient(160deg,#e4e6ea,#a7abb3 60%,#6e737c)}
  .post.c{left:225px;background:linear-gradient(160deg,#dcdde0,#a9a9ad 50%,#4b4c52)}
  .tag{position:absolute;left:10px;top:11px;background:var(--red);color:#fff;font-size:3.2px;padding:1px 6px;border-radius:3px}
  .post-meta{position:absolute;left:10px;top:55px;font-size:2.8px;color:#fff;opacity:.85}
  .post-head{position:absolute;left:10px;top:60px;width:70px;font-size:3.8px;font-weight:700;color:#fff;line-height:1.4}

  /* contact */
  .contact-title{left:36px;top:1219px}
  .contact-rule{left:0;top:1237px;width:154px}
  .field{left:37px;width:96px;border-bottom:.5px solid #d9dadb;font-size:3.4px;color:#bbb;padding-bottom:3px}
  .send{left:38px;top:1337px;width:41px;height:10px;border-radius:5px;background:var(--red);color:#fff;font-size:4px;text-align:center;line-height:10px}
  .map{left:175px;top:1193px;width:177px;height:169px;background:linear-gradient(135deg,#e7e8ea,#d5d6d9 50%,#e2e3e5)}

  /* footer */
  .footer{left:0;top:1362px;width:352px;height:70px;background:var(--dark)}
  .foot-brand{left:36px;top:1382px;display:flex;align-items:center;gap:3px}
  .foot-brand .brand-mark{width:9px;height:9px}
  .foot-brand span{font-size:6px;font-weight:600;color:#fff}
  .socials{left:38px;top:1403px;display:flex;gap:4px}
  .socials i{display:block;width:3.4px;height:3.4px;border-radius:50%;background:#9b9ca0}
  .foot-head{font-size:4.2px;color:var(--red);letter-spacing:.3px}
  .foot-links{font-size:3.4px;color:#b9babc;line-height:1.5;margin-top:5px}
  .newsletter{left:207px;top:1382px}
  .nl-input{left:207px;top:1399px;width:60px;height:9px;border-radius:5px;background:#4f5054;font-size:3.2px;color:#9a9a9e;padding-left:5px;line-height:9px}
  .nl-btn{left:263px;top:1399px;width:36px;height:9px;border-radius:5px;background:var(--red);color:#fff;font-size:3.8px;text-align:center;line-height:9px}
</style>
</head>
<body>
<div class="stage">
  <main class="site">

    <header class="abs topbar">
      <div class="abs brand">
        <span class="brand-mark"></span>
        <div class="brand-name">BRIGHT SUMMIT CONSULTING LLC<span class="brand-tag">Consulting &amp; Coaching</span></div>
      </div>
      <nav class="abs nav"><span>Home</span><span>Book Online</span><span>Client Login</span></nav>
    </header>

    <section class="abs hero" role="img" aria-label="Red-toned photo of business people talking in a meeting"></section>
    <h1 class="abs hero-title">IT'S <b>GROW</b> TIME</h1>
    <p class="abs hero-copy">From making strategic decisions to developing your capabilities, I'm here to help. Using my expertise and deep understanding of the industry, you'll receive real solutions and experience true results. Get in touch to book a meeting.</p>

    <div class="abs mist-band"></div>

    <section class="abs about-card"></section>
    <div class="abs ghost ghost-about">ABOUT</div>
    <div class="abs about-photo" role="img" aria-label="Video placeholder: black and white portrait of the coach at his desk"></div>
    <svg class="abs play" viewBox="0 0 40 40" aria-hidden="true">
      <circle cx="20" cy="20" r="19" fill="#9f1b14"/>
      <path d="M15 11 L29 20 L15 29 Z" fill="#fff"/>
    </svg>
    <h2 class="abs section-title about-title">My <span>Story</span></h2>
    <div class="abs rule about-rule"></div>
    <p class="abs about-copy">I've been a professional Business Coach since 2010. I believe in maintaining a positive mindset, creating partnerships with a purpose, and always striving for significant outcomes. When you work with me, you should expect a collaboration with transparency and consistency. Want to learn more? Contact me today for an initial consultation.</p>

    <div class="abs ghost ghost-feat">FEATURES</div>
    <h2 class="abs section-title feat-title">What <span>We Do</span></h2>
    <div class="abs rule feat-rule"></div>
    <div class="abs feat-img a" role="img" aria-label="Photo of an audience at a seminar"></div>
    <div class="abs feat-img b" role="img" aria-label="Photo of business people silhouetted by a window"></div>
    <div class="abs feat-img c" role="img" aria-label="Photo of a team discussing around a table"></div>
    <h3 class="abs feat-name" style="left:33px">BUSINESS PERFORMANCE<br>CONSULTING</h3>
    <h3 class="abs feat-name" style="left:132px">LEADERSHIP BUSINESS<br>COACHING</h3>
    <h3 class="abs feat-name" style="left:231px">SPEAKING AND TRAINING</h3>
    <p class="abs feat-copy" style="left:35px">By analyzing your systems, tools and people, I will identify strategies to get your business running at optimal efficiency. Book an introductory meeting today to learn more about how I can make your business thrive.</p>
    <p class="abs feat-copy" style="left:134px">Whether just starting out or looking to break through the next ceiling, we will work together on keeping you focused on the right measures that will generate measurable results. Contact me to find out how I can help today.</p>
    <p class="abs feat-copy" style="left:233px">Whether you need a simple keynote or a training package for your organization, we will collaborate with you as a partner to design a package to take your team to the next level. To find out more, get in touch.</p>

    <section class="abs stats"></section>
    <div class="abs stat" style="left:26px"><div class="stat-num">129</div><div class="stat-label">Finished Cases</div></div>
    <div class="abs stat" style="left:91px"><div class="stat-num">80+</div><div class="stat-label">Business Partners</div></div>
    <div class="abs stat" style="left:155px"><div class="stat-num">500</div><div class="stat-label">Happy Clients</div></div>
    <div class="abs cta">
      <div class="cta-kicker">GET IN TOUCH</div>
      <div class="cta-big">TODAY</div>
      <span class="pill">contact</span>
    </div>

    <h2 class="abs section-title book-title">Book <span>Online</span></h2>
    <div class="abs rule book-rule"></div>
    <div class="abs book-box" style="left:33px;width:91px" role="img" aria-label="Session image placeholder"><span class="pill">book</span></div>
    <div class="abs book-box" style="left:131px;width:90px" role="img" aria-label="Session image placeholder"><span class="pill">book</span></div>
    <div class="abs book-box" style="left:229px;width:90px" role="img" aria-label="Session image placeholder"><span class="pill">book</span></div>

    <section class="abs testi"></section>
    <div class="abs ghost ghost-testi">TESTIMONIALS</div>
    <h2 class="abs section-title testi-title">What <span>People Say</span></h2>
    <div class="abs rule testi-rule"></div>
    <p class="abs quote">Jordan was my first mentor and trainer in real estate. He pushed me from nobody to rookie of the year. He is the kind of person who brings out the best in you. I am forever grateful for his coaching and mentorship!</p>
    <p class="abs quote-by">Daniel Reyes</p>
    <div class="abs dots"><i></i><i></i><i class="on"></i></div>

    <section class="abs blog"></section>
    <div class="abs ghost ghost-news">NEWS</div>
    <h2 class="abs blog-title">Our <span>Blog</span></h2>
    <div class="abs rule blog-rule"></div>
    <article class="abs post a" role="img" aria-label="Blog photo of colleagues working at laptops">
      <span class="tag">Business</span>
      <span class="post-meta">June 12, 2019</span>
      <h3 class="post-head">Software Defined Networking in Business Security</h3>
    </article>
    <article class="abs post b" role="img" aria-label="Blog photo of a presenter at a whiteboard">
      <span class="tag">Strategy</span>
      <span class="post-meta">June 08, 2019</span>
      <h3 class="post-head">The Unexpected Channel in Marketing Research</h3>
    </article>
    <article class="abs post c" role="img" aria-label="Blog photo of a businessman in a suit">
      <span class="tag">Growth</span>
      <span class="post-meta">June 02, 2019</span>
      <h3 class="post-head">Transform the Customer Experience Journey</h3>
    </article>

    <h2 class="abs section-title contact-title">Let's Work <span>Together</span></h2>
    <div class="abs rule contact-rule"></div>
    <div class="abs field" style="top:1258px">Name</div>
    <div class="abs field" style="top:1276px">Email</div>
    <div class="abs field" style="top:1294px;height:30px">Message</div>
    <div class="abs send">send</div>
    <div class="abs map" role="img" aria-label="Street map showing the office location"></div>

    <footer class="abs footer"></footer>
    <div class="abs foot-brand"><span class="brand-mark"></span><span>Bright Summit</span></div>
    <div class="abs socials"><i></i><i></i><i></i><i></i></div>
    <div class="abs" style="left:125px;top:1382px">
      <div class="foot-head">QUICK LINKS</div>
      <div class="foot-links">Book Online<br>Client Login<br>Contact</div>
    </div>
    <div class="abs newsletter"><div class="foot-head">NEWSLETTER</div></div>
    <div class="abs nl-input">Your email</div>
    <div class="abs nl-btn">Sign up</div>

  </main>
</div>
</body>
</html>
```